High-end construction company needs a business card design

We need a modern looking business card that draws people in, is memorable and looks so good people will want to sick it on their fridges.
On the first side what is needed are:
Logo
My name - Tomas Verbelk
Title - Managing Director
Website - www.kravel.co.uk
Email - tomas@kravel.co.uk
Telephone - 020 5194 6381
Mobile - 07845319027
On the back side was is needed is a list of all the services we provide:
-Kitchen Renovations
-Bathroom Renovations
-House Renovations
-Garage Conversions
-Extensions
-Loft Conversions
-Conservatories
-Carpentry
-Tiling
-Electrical
-Plumbing & Heating
-Bricklaying
-Landscaping
-Decorating
-Plastering
We would like the colours to be the same shades as on the logo with grey or black for the words.
Target Market(s)
Anyone who needs building work done
Contact Information for Business Card
This business card is for a construction company which strives to deliver excellent service and quality.
The look and feel of the card should represent this.
Requirements
Must have
- On the first side what is needed are:
Logo
My name - Tomas Verbelk
Title - Managing Director
Website - www.kravel.co.uk
Email - tomas@kravel.co.uk
Telephone - 020 5194 6381
Mobile - 07845319027
Nice to have
- Cool looking features

```html
<!DOCTYPE html>
<html lang="en">
<head>
<meta charset="utf-8">
<title>Kravel Construction – Business Card</title>
<link rel="stylesheet" href="https://fonts.googleapis.com/css2?family=Montserrat:wght@400;500;700;800&display=swap">
<style>
  :root {
    --page-bg: #e6e8e6;
    --green-light: #79c043;
    --green: #5aaa3c;
    --green-deep: #3f8f3a;
    --white: #ffffff;
    --ink: #555a5e;
    --ink-soft: #7a7f83;
    --rule: #8cc862;
  }
  * { box-sizing: border-box; margin: 0; padding: 0; }
  html, body { width: 1200px; height: 880px; overflow: hidden; }
  body {
    background: var(--page-bg);
    font-family: "Montserrat", sans-serif;
    position: relative;
  }
  .card {
    position: absolute;
    width: 680px;
    height: 390px;
    border-radius: 22px;
    box-shadow: 0 10px 30px rgba(0,0,0,0.18);
    overflow: hidden;
  }
  /* back side */
  .card-back {
    left: 70px; top: 40px;
    background: linear-gradient(160deg, var(--green-light) 0%, var(--green) 55%, var(--green-deep) 100%);
    color: var(--white);
  }
  .services {
    position: absolute;
    left: 46px; top: 42px;
    list-style: none;
    font-size: 17px;
    font-weight: 500;
    letter-spacing: 0.6px;
    line-height: 20.5px;
  }
  .services li { position: relative; padding-left: 20px; }
  .services li::before {
    content: "";
    position: absolute; left: 0; top: 6px;
    width: 8px; height: 8px; border-radius: 50%;
    background: var(--white);
  }
  .card-back .brand { position: absolute; right: 52px; top: 80px; text-align: left; }
  .card-back .brand-name { color: var(--white); }
  .card-back .site {
    position: absolute; right: 48px; bottom: 48px;
    font-size: 17px; letter-spacing: 0.6px;
  }
  .card-back .site b { font-weight: 800; }

  /* shared brand name */
  .brand { display: flex; align-items: center; gap: 12px; }
  .brand-mark { width: 16px; height: 16px; flex: none; }
  .brand-name {
    font-weight: 800;
    font-size: 30px;
    line-height: 1.05;
    letter-spacing: 1px;
    text-transform: uppercase;
  }
  .brand-name small { display: block; font-size: 15px; letter-spacing: 2.4px; }

  /* front side */
  .card-front {
    left: 450px; top: 460px;
    background: var(--white);
    color: var(--ink);
  }
  .card-front .brand { position: absolute; left: 60px; top: 160px; }
  .card-front .brand-mark { background: var(--green); }
  .card-back .brand-mark { background: var(--white); }
  .card-front .brand-name { color: var(--green); }
  .divider {
    position: absolute; left: 352px; top: 70px;
    width: 1.5px; height: 250px;
    background: linear-gradient(to bottom, transparent, var(--rule) 20%, var(--rule) 80%, transparent);
  }
  .person { position: absolute; left: 384px; top: 92px; }
  .person-name {
    color: var(--green);
    font-weight: 800;
    font-size: 24px;
    letter-spacing: 0.5px;
    text-transform: uppercase;
  }
  .person-title { font-size: 15px; color: var(--ink-soft); margin-top: 2px; }
  .contacts { list-style: none; margin-top: 22px; }
  .contacts li {
    display: flex; align-items: center; gap: 12px;
    font-size: 16px; line-height: 27px; color: var(--ink);
  }
  .contacts svg { width: 18px; height: 18px; flex: none; }
  .contacts .accent { color: var(--green); }
</style>
</head>
<body>

<section class="card card-back" aria-label="Card back – services">
  <ul class="services">
    <li>Kitchen Renovations</li>
    <li>Bathroom Renovations</li>
    <li>House Renovations</li>
    <li>Garage Conversions</li>
    <li>Extensions</li>
    <li>Loft Conversions</li>
    <li>Conservatories</li>
    <li>Carpentry</li>
    <li>Tiling</li>
    <li>Electrical</li>
    <li>Plumbing &amp; Heating</li>
    <li>Bricklaying</li>
    <li>Landscaping</li>
    <li>Decorating</li>
    <li>Plastering</li>
  </ul>
  <div class="brand">
    <span class="brand-mark"></span>
    <span class="brand-name">Kravel<small>Construction Ltd</small></span>
  </div>
  <p class="site">www.<b>kravel</b>.co.uk</p>
</section>

<section class="card card-front" aria-label="Card front – contact details">
  <div class="brand">
    <span class="brand-mark"></span>
    <span class="brand-name">Kravel<small>Construction Ltd</small></span>
  </div>
  <div class="divider"></div>
  <div class="person">
    <h1 class="person-name">Tomas Verbelk</h1>
    <p class="person-title">Managing Director</p>
    <ul class="contacts">
      <li>
        <svg viewBox="0 0 18 18" aria-hidden="true"><circle cx="9" cy="9" r="8.5" fill="#5aaa3c"/><path d="M6 5.2c.4-.4 1-.4 1.3 0l.8 1c.3.4.2.9-.1 1.2l-.5.4c.4.9 1.1 1.6 2 2l.4-.5c.3-.3.8-.4 1.2-.1l1 .8c.4.3.4.9 0 1.3l-.6.6C10 13.2 5 8.2 5.4 5.8z" fill="#fff"/></svg>
        020 5194 6381
      </li>
      <li>
        <svg viewBox="0 0 18 18" aria-hidden="true"><circle cx="9" cy="9" r="8.5" fill="#5aaa3c"/><rect x="6.3" y="4.3" width="5.4" height="9.4" rx="1" fill="none" stroke="#fff" stroke-width="1.2"/><circle cx="9" cy="12" r=".6" fill="#fff"/></svg>
        07845319027
      </li>
      <li>
        <svg viewBox="0 0 18 18" aria-hidden="true"><circle cx="9" cy="9" r="8.5" fill="#5aaa3c"/><rect x="4.8" y="6" width="8.4" height="6" rx=".6" fill="none" stroke="#fff" stroke-width="1.1"/><path d="M5 6.3l4 3 4-3" fill="none" stroke="#fff" stroke-width="1.1"/></svg>
        tomas@kravel.co.uk
      </li>
      <li>
        <svg viewBox="0 0 18 18" aria-hidden="true"><circle cx="9" cy="9" r="8.5" fill="#5aaa3c"/><circle cx="9" cy="9" r="4.4" fill="none" stroke="#fff" stroke-width="1.1"/><path d="M4.6 9h8.8M9 4.6c-2 2.4-2 6.4 0 8.8M9 4.6c2 2.4 2 6.4 0 8.8" fill="none" stroke="#fff" stroke-width="1"/></svg>
        <span>www.<span class="accent">kravel</span>.co.uk</span>
      </li>
    </ul>
  </div>
</section>

</body>
</html>
```